Business Card Design

We are an IT staffing and consulting company providing IT solutions and resources to our clients.

Industry/Entity Type

Business

Contact Information for Business Card

Ramesh Tulavarthi
Vice President

BrightNode Inc
48215 Harrowmere Court Square, suite 700
Ashburn, VA 20147
Direct: 571-555-0193
Mobile: 571-555-0147
Email: Ramesh@brightnodeinc.com
Fax: 703-555-0162
www.brightnodeinc.com

```html
<!DOCTYPE html>
<html lang="en">
<head>
<meta charset="utf-8">
<title>BrightNode Inc – Business Card</title>
<link rel="stylesheet" href="https://fonts.googleapis.com/css2?family=Open+Sans:wght@400;700&display=swap">
<style>
  :root {
    --backdrop: #e4e4e4;
    --card: #ffffff;
    --ink: #2b2b2b;
    --ink-soft: #444444;
    --brand-red: #b0251c;
    --band-dark: #1e1e1e;
    --shadow: rgba(0, 0, 0, 0.18);
  }
  * { box-sizing: border-box; margin: 0; padding: 0; }
  html, body {
    width: 1200px;
    height: 852px;
    overflow: hidden;
    background: var(--backdrop);
    font-family: "Open Sans", Arial, sans-serif;
    color: var(--ink);
  }
  .stage {
    position: relative;
    width: 1200px;
    height: 852px;
  }
  .card {
    position: absolute;
    width: 520px;
    height: 298px;
    background: var(--card);
    border-radius: 24px;
    box-shadow: 0 6px 18px var(--shadow);
    overflow: hidden;
  }
  .card--front { left: 60px; top: 190px; }
  .card--back  { left: 620px; top: 364px; }

  .brand {
    display: flex;
    align-items: center;
    gap: 10px;
  }
  .brand__dot {
    width: 16px;
    height: 16px;
    border-radius: 50%;
    background: var(--brand-red);
  }
  .brand__name {
    font-weight: 400;
    color: var(--ink);
    letter-spacing: 0.5px;
  }
  .card--front .brand {
    position: absolute;
    left: 50%;
    top: 50%;
    transform: translate(-50%, -50%);
  }
  .card--front .brand__name { font-size: 44px; }
  .card--front .brand__dot { width: 22px; height: 22px; }

  .card--back .brand {
    position: absolute;
    right: 30px;
    top: 28px;
  }
  .card--back .brand__name { font-size: 30px; }

  .band {
    position: absolute;
    left: 0;
    top: 0;
    bottom: 0;
    width: 46px;
    background: var(--brand-red);
    border-right: 5px solid var(--band-dark);
  }

  .person {
    position: absolute;
    left: 72px;
    top: 92px;
  }
  .person__name {
    font-size: 17px;
    font-weight: 700;
    color: var(--brand-red);
  }
  .person__title {
    font-size: 13px;
    color: var(--ink-soft);
    margin-top: 2px;
  }

  .address {
    position: absolute;
    left: 72px;
    top: 152px;
    font-size: 12px;
    line-height: 1.45;
    color: var(--ink-soft);
  }

  .contacts {
    position: absolute;
    left: 72px;
    top: 192px;
    list-style: none;
    font-size: 12px;
    color: var(--ink-soft);
  }
  .contacts li {
    display: flex;
    align-items: center;
    gap: 10px;
    height: 19px;
  }
  .contacts svg {
    width: 12px;
    height: 12px;
    fill: var(--brand-red);
    flex: none;
  }
  .contacts .accent { color: var(--brand-red); }
</style>
</head>
<body>
<main class="stage">

  <section class="card card--front" aria-label="Business card front">
    <div class="brand">
      <span class="brand__dot"></span>
      <span class="brand__name">BrightNode</span>
    </div>
  </section>

  <section class="card card--back" aria-label="Business card back">
    <div class="band"></div>

    <div class="brand">
      <span class="brand__dot"></span>
      <span class="brand__name">BrightNode</span>
    </div>

    <div class="person">
      <p class="person__name">Ramesh Tulavarthi</p>
      <p class="person__title">Vice President</p>
    </div>

    <p class="address">48215 Harrowmere Court Square,<br>suite 700 Ashburn, VA 20147</p>

    <ul class="contacts">
      <li>
        <svg viewBox="0 0 12 12" aria-hidden="true"><path d="M2 1h2.5l1 2.5-1.5 1a6 6 0 0 0 3.5 3.5l1-1.5 2.5 1V11c-5 0-9-4-9-9z"/></svg>
        571-555-0193
      </li>
      <li>
        <svg viewBox="0 0 12 12" aria-hidden="true"><path d="M3 0h6v12H3zM4 1.5v8h4v-8z"/><circle cx="6" cy="10.8" r=".6" fill="#fff"/></svg>
        571-555-0147
      </li>
      <li>
        <svg viewBox="0 0 12 12" aria-hidden="true"><path d="M3 0h6v3H3zM1 4h10v5H9v3H3V9H1zM4 8v3h4V8z"/></svg>
        703-555-0162
      </li>
      <li>
        <svg viewBox="0 0 12 12" aria-hidden="true"><path d="M0 2h12v8H0zM1 3l5 4 5-4v-.2H1z"/></svg>
        Ramesh@brightnodeinc.com
      </li>
      <li>
        <svg viewBox="0 0 12 12" aria-hidden="true"><circle cx="6" cy="6" r="5.5"/><path d="M.5 6h11M6 .5c-3 3-3 8 0 11M6 .5c3 3 3 8 0 11" stroke="#fff" stroke-width=".8" fill="none"/></svg>
        <span>www.<span class="accent">brightnodeinc</span>.com</span>
      </li>
    </ul>
  </section>

</main>
</body>
</html>
```